Web Design Project - vR Advise

We want to modernise our web page profile. We have an existing web site that we are particularly not proud of (www.vradvise.com.au).
We have started to build a new web site using Joomla and we like the structure of it, but we need it to be professionally designed and implemented.

This current development site can be viewed here: dev.vradvise.com.au

We would like a complete design for the entire website, ready for deployment.

(We still need to finalise the content, as we have just developed new products that we hope to launch in August both on this web site and by a Vendor Forum.)
Updates

Target Market(s)

Larger companies where the robustness of their IT infrastructure is critical. Our tools and services provide for monitoring of every device

Industry/Entity Type

Build

Requirements
Must have
• Responsive design for different screen sizes.

BrightDock help desk software integrated with the website.
Currently can be viewed at support.vradvise.com.au
Brightdock only supports custom css.

Nice to have
• Customer experience testimonials in a rotating banner
Chirpr and Pagebook links in the footer
We use Avenir as a company font.
Use company colours as in the logo (green and blue)

```html
<!DOCTYPE html>
<html lang="en">
<head>
<meta charset="utf-8">
<title>vR Advise</title>
<link rel="stylesheet" href="https://fonts.googleapis.com/css2?family=Ubuntu:ital,wght@0,400;0,500;0,700;1,500;1,700&family=Open+Sans:wght@400;600&display=swap">
<style>
:root{
  --green:#72a832;
  --blue:#1a8fd0;
  --header-grey:#f7f7f7;
  --text:#3c3c3c;
  --nav-text:#4a4a4a;
  --lime:#d8f23a;
  --consulting:#9c2f6f;
  --professional:#3cb4a9;
  --productised:#994a30;
  --products:#2e8a9c;
  --vendor:#6d9a2f;
  --social:#8aa7b8;
  --footer:#262626;
  --footer-bottom:#151515;
  --footer-text:#b8b8b8;
}
*{margin:0;padding:0;box-sizing:border-box}
html,body{width:971px;height:1200px;overflow:hidden;background:#fff}
body{position:relative;font-family:"Open Sans",sans-serif;color:var(--text)}
.abs{position:absolute}
.site-header{left:0;top:17px;width:971px;height:147px;background:var(--header-grey)}
.brand{left:140px;top:68px;display:flex;align-items:center;gap:8px;font-family:"Ubuntu",sans-serif;font-weight:700;font-size:22px;color:var(--blue)}
.brand-dot{width:28px;height:28px;border-radius:50%;background:var(--green)}
.search{left:618px;top:67px;width:203px;height:25px;background:#efefef;border-radius:2px}
.search svg{position:absolute;right:6px;top:5px}
.main-nav{left:0;top:164px;width:971px;height:49px;background:#fff}
.nav-item{position:absolute;top:0;height:49px;line-height:56px;font-family:"Ubuntu",sans-serif;font-weight:500;font-size:10.5px;color:var(--nav-text);text-transform:uppercase;transform:translateX(-50%)}
.nav-item.active{left:150px;width:108px;top:7px;height:42px;line-height:42px;transform:none;background:var(--green);color:#fff;text-align:center}
.hero{left:0;top:213px;width:971px;height:289px;background:linear-gradient(180deg,#1e8fcf 0%,#148ccd 60%,#1a93d3 100%)}
.hero-title{left:0;top:112px;width:971px;text-align:center;font-family:"Ubuntu",sans-serif;font-style:italic;font-weight:700;font-size:39px;color:#fff;letter-spacing:.2px}
.hero-title em{color:var(--lime);font-style:italic}
.hero-sub{left:0;top:170px;width:971px;text-align:center;font-family:"Ubuntu",sans-serif;font-weight:500;font-size:16px;color:#fff}
.hero-arrow{top:141px;width:31px;height:32px;background:rgba(255,255,255,.35);display:flex;align-items:center;justify-content:center}
.service-card{top:523px;width:126px;height:173px;border-radius:2px;color:#fff;padding:17px 11px 0}
.service-card h3{font-family:"Ubuntu",sans-serif;font-weight:700;font-size:13px;line-height:12px;text-align:center;text-transform:uppercase}
.service-card p{margin-top:13px;font-size:7.4px;line-height:11px;text-align:justify}
.card-go{position:absolute;right:14px;bottom:12px;width:17px;height:17px;border-radius:50%;background:#fff;display:flex;align-items:center;justify-content:center}
.welcome{left:161px;top:724px;width:660px}
.welcome h2{font-family:"Ubuntu",sans-serif;font-weight:500;font-size:12.5px;color:#3a3a3a}
.welcome p{margin-top:13px;font-size:8.6px;line-height:11.2px;color:#444;text-align:justify}
.welcome p+p{margin-top:11px}
.social{left:845px;width:22px;height:22px;border-radius:3px;background:var(--social)}
.partner{top:896px;display:flex;align-items:center;gap:6px;font-family:"Ubuntu",sans-serif;font-weight:500;font-size:15px;color:#2b4f8a;transform:translateX(-50%)}
.partner i{display:block;width:16px;height:16px;border-radius:50%;background:#2b8ac4}
.partner-arrow{top:895px;font-size:18px;color:#555}
.site-footer{left:0;top:952px;width:971px;height:210px;background:var(--footer)}
.footer-col{top:36px;font-family:"Ubuntu",sans-serif}
.footer-col h4{font-weight:500;font-size:11px;color:#eee;margin-bottom:9px}
.footer-col li{list-style:none;font-size:9.8px;line-height:16.8px;color:var(--footer-text)}
.footer-col.follow li{line-height:14px}
.bullet{left:156px;top:1011px;color:var(--green);font-size:10px;font-family:"Ubuntu",sans-serif}
.footer-bottom{left:0;top:1162px;width:971px;height:38px;background:var(--footer-bottom);border-bottom:2px solid var(--green)}
.copyright{left:152px;top:14px;font-family:"Ubuntu",sans-serif;font-size:8.5px;color:#ccc}
</style>
</head>
<body>
<header class="abs site-header"></header>
<div class="abs brand"><span class="brand-dot"></span>vR Advise</div>
<div class="abs search">
  <svg width="14" height="14" viewBox="0 0 14 14"><circle cx="5.5" cy="5.5" r="4" fill="none" stroke="#333" stroke-width="1.6"/><line x1="8.5" y1="8.5" x2="13" y2="13" stroke="#333" stroke-width="2"/></svg>
</div>

<nav class="abs main-nav">
  <span class="nav-item active">Home</span>
  <span class="nav-item" style="left:305px">Services</span>
  <span class="nav-item" style="left:408px">Support</span>
  <span class="nav-item" style="left:517px">Ptroducts</span>
  <span class="nav-item" style="left:633px">About Us</span>
  <span class="nav-item" style="left:759px">Contact</span>
</nav>

<section class="abs hero" role="img" aria-label="Blue banner with faint technical drawing of equipment dimensions">
  <div class="abs hero-title">Any <em>Device</em>, Any <em>Platform</em>, <em>Anywhere</em></div>
  <div class="abs hero-sub">Cross-domain, performance and service level monitoring and management</div>
  <div class="abs hero-arrow" style="left:89px"><svg width="10" height="14" viewBox="0 0 10 14"><polyline points="7,2 3,7 7,12" fill="none" stroke="#fff" stroke-width="2.4"/></svg></div>
  <div class="abs hero-arrow" style="left:843px"><svg width="10" height="14" viewBox="0 0 10 14"><polyline points="3,2 7,7 3,12" fill="none" stroke="#fff" stroke-width="2.4"/></svg></div>
</section>

<article class="abs service-card" style="left:150px;background:var(--consulting)">
  <h3>Consulting Services</h3>
  <p>Lorem ipsum dolor sit amet, consectetuer adipiscing Nam cursus. Morbi ut mi. Nullam enim leo, egestas id, condimentum at, laoreet mattis, massa. Sed eleifend nonummy diam. amet, nibh.</p>
  <span class="card-go"><svg width="6" height="8" viewBox="0 0 6 8"><polyline points="1.5,1 4.5,4 1.5,7" fill="none" stroke="#333" stroke-width="1.4"/></svg></span>
</article>
<article class="abs service-card" style="left:286px;background:var(--professional)">
  <h3>Professional Services</h3>
  <p>Lorem ipsum dolor sit amet, consectetuer adipiscing Nam cursus. Morbi ut mi. Nullam enim leo, egestas id, condimentum at, laoreet mattis, massa. Sed eleifend nonummy diam. amet, nibh.</p>
  <span class="card-go"><svg width="6" height="8" viewBox="0 0 6 8"><polyline points="1.5,1 4.5,4 1.5,7" fill="none" stroke="#333" stroke-width="1.4"/></svg></span>
</article>
<article class="abs service-card" style="left:422px;background:var(--productised)">
  <h3>Productised Services</h3>
  <p>Lorem ipsum dolor sit amet, consectetuer adipiscing Nam cursus. Morbi ut mi. Nullam enim leo, egestas id, condimentum at, laoreet mattis, massa. Sed eleifend nonummy diam. amet, nibh.</p>
  <span class="card-go"><svg width="6" height="8" viewBox="0 0 6 8"><polyline points="1.5,1 4.5,4 1.5,7" fill="none" stroke="#333" stroke-width="1.4"/></svg></span>
</article>
<article class="abs service-card" style="left:558px;background:var(--products)">
  <h3>vR Advise Products</h3>
  <p>Lorem ipsum dolor sit amet, consectetuer adipiscing Nam cursus. Morbi ut mi. Nullam enim leo, egestas id, condimentum at, laoreet mattis, massa. Sed eleifend nonummy diam. amet, nibh.</p>
  <span class="card-go"><svg width="6" height="8" viewBox="0 0 6 8"><polyline points="1.5,1 4.5,4 1.5,7" fill="none" stroke="#333" stroke-width="1.4"/></svg></span>
</article>
<article class="abs service-card" style="left:694px;background:var(--vendor)">
  <h3>Vendor Products</h3>
  <p>Lorem ipsum dolor sit amet, consectetuer adipiscing Nam cursus. Morbi ut mi. Nullam enim leo, egestas id, condimentum at, laoreet mattis, massa. Sed eleifend nonummy diam. amet, nibh.</p>
  <span class="card-go"><svg width="6" height="8" viewBox="0 0 6 8"><polyline points="1.5,1 4.5,4 1.5,7" fill="none" stroke="#333" stroke-width="1.4"/></svg></span>
</article>

<section class="abs welcome">
  <h2>WELCOME TO VR ADVISE !</h2>
  <p>Lorem ipsum dolor sit amet, consectetuer adipiscing elit. Nam cursus. Morbi ut mi. Nullam enim leo, egestas id, condimentum at, laoreet mattis, massa. Sed eleifend nonummy diam. Praesent mauris ante, elementum et, bibendum at, posuere sit amet, nibh.Lorem ipsum dolor sit amet, consectetuer adipiscing elit. Nam cursus. Morbi ut mi. Nullam enim leo, egestas id, condimentum at, laoreet mattis, massa. Lorem ipsum dolor sit amet, consectetuer adipiscing elit. Nam cursus. Morbi ut mi. Nullam enim leo, egestas id, condimentum at, laoreet mattis, massa. Sed eleifend nonummy diam.</p>
  <p>Praesent mauris ante, elementum et, bibendum at, posuere sit amet, nibh.Lorem ipsum dolor sit amet, consectetuer adipiscing elit. Nam cursus. Morbi ut mi. Nullam enim leo, egestas id, condimentum at, laoreet mattis, massa.Lorem ipsum dolor sit amet, consectetuer adipiscing elit. Nam cursus. Morbi ut mi. Nullam enim leo, egestas id, condimentum at, laoreet mattis, massa. Sed eleifend nonummy diam. Praesent mauris ante, elementum et, bibendum at, posuere sit amet, nibh.Lorem ipsum dolor sit amet, consectetuer adipiscing elit. Nam cursus. Morbi ut mi. Nullam enim leo, egestas id, condimentum at, laoreet mattis, massa.</p>
</section>

<a class="abs social" style="top:767px" aria-label="Chirpr"></a>
<a class="abs social" style="top:797px" aria-label="Pagebook"></a>
<a class="abs social" style="top:827px" aria-label="Clipstage"></a>

<span class="abs partner-arrow" style="left:99px">&#10094;</span>
<div class="abs partner" style="left:178px"><i></i>Norvia</div>
<div class="abs partner" style="left:324px"><i></i>Keystone Pay</div>
<div class="abs partner" style="left:484px"><i></i>Billvo</div>
<div class="abs partner" style="left:644px"><i></i>Marlow</div>
<div class="abs partner" style="left:787px"><i></i>Linkwave</div>
<span class="abs partner-arrow" style="left:855px">&#10095;</span>

<footer class="abs site-footer">
  <div class="abs footer-col" style="left:172px"><h4>Quick Links</h4><ul><li>Home</li><li>Services</li><li>Support</li><li>Products</li><li>Contact&nbsp; Us</li><li>About Us</li><li>Privacy Policy</li></ul></div>
  <div class="abs footer-col" style="left:306px"><h4>Support</h4><ul><li>Consulting Services</li><li>Professional Services</li><li>Productised Services</li><li>vR Advise Products</li><li>Vendor Products</li><li>Operational Support</li><li>Training</li></ul></div>
  <div class="abs footer-col" style="left:454px"><h4>Products</h4><ul><li>Consulting Services</li><li>Professional Services</li><li>Productised Services</li><li>vR Advise Products</li><li>Vendor Products</li><li>Operational Support</li><li>Training</li></ul></div>
  <div class="abs footer-col" style="left:602px"><h4>Services</h4><ul><li>Consulting Services</li><li>Professional Services</li><li>Productised Services</li><li>vR Advise Products</li><li>Vendor Products</li><li>Operational Support</li><li>Training</li></ul></div>
  <div class="abs footer-col follow" style="left:758px"><h4>Follow Us</h4><ul><li>Chirpr</li><li>Pagebook</li><li>Clipstage</li></ul></div>
</footer>
<span class="abs bullet">&raquo;</span>
<div class="abs footer-bottom"><span class="abs copyright">&copy; 2013 vR Advise. All Rights Reserved.</span></div>
</body>
</html>
```